Calder Bros (logo) and Premium Tessel Potatoes (package design)

Design a brand logo for Calder Bros, and create a package design (face panel only) for a bag of Premium Tessel Potatoes.

Attached is a quick concept to give you a rough idea. However, we would like it be more unique and not so common as the idea shown. It needs to be PREMIUM as these are slightly higher priced potatoes. And the packaging needs to look different than the typical potato bags. The brand story is the Calder brothers have been farming potatoes in Ireland for four generations. They are now creating their own brand and will market the best potatoes available in Ireland (shape, no blemishes, color, taste, size, etc.). The type of potato is Tessel.

There will be a window in the front panel to show the product behind netting. Use the other image (Dunbrook Potatoes) as a guide to the bag shape (face panel only) and location of the window.

The bag can be any color, and you can design with any photos/images/etc. that are royalty free. The tear strip across the top can be any color, too.

Reason: Time extended. But please submits within the next day or two at the latest due to print deadline. Thanks!

Target Market(s)

Moms with families

Industry/Entity Type

Farming

Font styles to use
Serif

Requirements
Must have
• Calder Bros logo
• Premium Tessel Potatoes (copy)
• Window to show product (potatoes)
• Bag Net Weight: 10 kg
• Dimensions: 22 inches high and 10.5 wide
Nice to have
• Brand name/logo must be readable and large on the bag
• Bag should stand out and be unique
• Be premium looking, including colors
• OK to explore a vintage tractor, image of a rooster, family farm, as a couple of ideas.
• Open to all ideas; do not be limited to the above ideas
Should not have
• Should not look like a generic bag of potatoes

```html
<!DOCTYPE html>
<html lang="en">
<head>
<meta charset="utf-8">
<title>Calder Bros – Premium Tessel Potatoes, 10 kg face panel</title>
<link rel="stylesheet" href="https://fonts.googleapis.com/css2?family=Abril+Fatface&family=Oswald:wght@300;600&display=swap">
<style>
  :root {
    --navy: #232c47;
    --navy-soft: rgba(35, 44, 71, 0.88);
    --sky-top: #8fb6db;
    --sky-low: #c9dcea;
    --hill: #a9a68a;
    --hill-shadow: #7d7f66;
    --field-far: #4e6a38;
    --field-mid: #3a5a2a;
    --field-near: #2b4621;
    --silver-dark: #8f9296;
    --silver-light: #f1f2f3;
    --window: #ffffff;
    --white: #ffffff;
  }
  html, body {
    margin: 0;
    padding: 0;
    width: 1200px;
    height: 2513px;
    overflow: hidden;
    background: #ffffff;
  }
  .face-panel {
    position: relative;
    width: 1200px;
    height: 2513px;
    overflow: hidden;
  }
  .farm-scene {
    position: absolute;
    inset: 0;
    background: linear-gradient(180deg,
      var(--sky-top) 0%,
      var(--sky-low) 15%,
      var(--hill) 18%,
      var(--hill-shadow) 28%,
      var(--hill) 31%,
      var(--field-far) 33%,
      var(--field-mid) 55%,
      var(--field-near) 100%);
  }
  .bands {
    position: absolute;
    inset: 0;
  }
  .brand-name {
    position: absolute;
    left: 0;
    width: 1200px;
    top: 450px;
    margin: 0;
    text-align: center;
    font-family: "Oswald", "Arial Narrow", sans-serif;
    font-weight: 600;
    font-size: 170px;
    line-height: 1;
    letter-spacing: 6px;
    text-transform: uppercase;
    color: var(--navy);
  }
  .product-plate {
    position: absolute;
    left: 168px;
    top: 1001px;
    width: 910px;
    height: 308px;
  }
  .product-plate svg {
    position: absolute;
    inset: 0;
  }
  .product-title {
    position: absolute;
    inset: 0;
    margin: 0;
    text-align: center;
    color: var(--navy);
  }
  .product-title .grade {
    position: absolute;
    left: 0;
    right: 0;
    top: 18px;
    font-family: "Abril Fatface", Georgia, serif;
    font-weight: 400;
    font-size: 140px;
    line-height: 1;
  }
  .product-title .variety {
    position: absolute;
    left: 0;
    right: 0;
    top: 162px;
    font-family: "Oswald", "Arial Narrow", sans-serif;
    font-weight: 600;
    font-size: 96px;
    line-height: 1;
    letter-spacing: 3px;
  }
  .product-window {
    position: absolute;
    left: 387px;
    top: 1350px;
    width: 430px;
    height: 817px;
    border-radius: 215px;
    background: var(--window);
    box-shadow: 0 0 0 4px rgba(255,255,255,0.5), 0 4px 14px rgba(0,0,0,0.45);
  }
  .net-weight {
    position: absolute;
    left: 0;
    width: 1200px;
    top: 2278px;
    margin: 0;
    text-align: center;
    font-family: "Oswald", "Arial Narrow", sans-serif;
    font-weight: 300;
    font-size: 48px;
    letter-spacing: 1px;
    color: var(--white);
  }
  .net-weight .divider {
    margin: 0 22px;
  }
  .weight-flourish {
    position: absolute;
    left: 346px;
    top: 2356px;
    width: 508px;
    height: 44px;
    border-radius: 22px;
    background: linear-gradient(90deg, rgba(255,255,255,0), rgba(255,255,255,0.35), rgba(255,255,255,0));
  }
</style>
</head>
<body>
<main class="face-panel">
  <div class="farm-scene" role="img" aria-label="Photo of green potato field rows under blue sky with rolling hills"></div>

  <svg class="bands" width="1200" height="2513" viewBox="0 0 1200 2513" aria-hidden="true">
    <polygon points="0,0 1200,0 1200,38 0,247" fill="var(--navy)"/>
    <polygon points="0,2251 1200,2115 1200,2513 0,2513" fill="var(--navy-soft)"/>
  </svg>

  <h1 class="brand-name">Calder Bros</h1>

  <div class="product-plate">
    <svg width="910" height="308" viewBox="0 0 910 308" aria-hidden="true">
      <defs>
        <linearGradient id="plate-silver" x1="0" y1="0" x2="1" y2="1">
          <stop offset="0" stop-color="var(--silver-light)"/>
          <stop offset="0.5" stop-color="#c9cbce"/>
          <stop offset="1" stop-color="var(--silver-light)"/>
        </linearGradient>
      </defs>
      <polygon points="30,0 880,0 910,30 910,278 880,308 30,308 0,278 0,30" fill="var(--silver-dark)"/>
      <polygon points="38,10 872,10 900,38 900,270 872,298 38,298 10,270 10,38" fill="#fafafa"/>
      <polygon points="46,20 864,20 888,44 888,264 864,288 46,288 22,264 22,44" fill="url(#plate-silver)"/>
      <line x1="100" y1="156" x2="810" y2="156" stroke="var(--navy)" stroke-width="5"/>
    </svg>
    <h2 class="product-title">
      <span class="grade">PREMIUM</span>
      <span class="variety">TESSEL POTATOES</span>
    </h2>
  </div>

  <div class="product-window" aria-label="Window showing potatoes behind netting"></div>

  <p class="net-weight">10KG<span class="divider">|</span>NET WEIGHT</p>
  <div class="weight-flourish" role="img" aria-label="Decorative flourish under net weight"></div>
</main>
</body>
</html>
```